GPS Tracker Business Card Design

We need a business card for a GPS Vehicle tracking company. We sell the hardware for the vehicle and the software platform to monitor your vehicle/s. Including high asset non-powered vehicles like a trailer using our solar powered unit.
We like using dark blue to different shades of blue along with gold. We have phone apps for Android and Apple devices.

We have a platform for families wanting to track their teenage driver and children; Plus a Fleet vehicle tracking platform.

Features: unlimited number of vehicles and/or assets including snow mobiles forklifts generators trailers airport equipment

Reports for driving behavior reports and alerts dashboard fleet maintenace timeline view and replay geofence real time alerts logbook scheduling route optimization accounting integration fleet grouping closest vehicle locator On Board Diagnostics.

Benefits: Increased productivity improved fuel efficiency organizing your business improve time management simplify back end processes, reduce fleet fuel efficiency and expenses increase fleet security etc..

Please view website: Velmorix.com

Industry/Entity Type

Business

Contact Information for Business Card

Harold P Simkins

```html
<!DOCTYPE html>
<html lang="en">
<head>
<meta charset="utf-8">
<title>Velmorix Business Card</title>
<link rel="stylesheet" href="https://fonts.googleapis.com/css2?family=Montserrat:wght@300&family=Open+Sans:wght@400;600&family=Roboto+Condensed:wght@400&display=swap">
<style>
  :root {
    --page-bg: #e9eaec;
    --card-white: #ffffff;
    --brand-blue: #0b4fa0;
    --accent-blue: #3b8fcb;
    --rule-blue: #5b95d6;
    --tagline-blue: #3f5f8c;
    --text-gray: #444a52;
    --text-dark: #1e2126;
    --white: #ffffff;
  }
  * { margin: 0; padding: 0; box-sizing: border-box; }
  html, body {
    width: 1105px; height: 1200px; overflow: hidden;
    background: var(--page-bg);
    font-family: "Open Sans", Arial, sans-serif;
  }
  .canvas { position: relative; width: 1105px; height: 1200px; }
  .card {
    position: absolute; left: 192px; width: 720px; height: 412px;
    box-shadow: 0 4px 14px rgba(0,0,0,0.18);
  }
  .card-front { top: 146px; background: var(--card-white); }
  .card-back { top: 602px; background: var(--brand-blue); color: var(--white); }

  .brand { position: absolute; }
  .brand-name {
    font-family: "Montserrat", Arial, sans-serif; font-weight: 300;
    font-size: 62px; line-height: 1; letter-spacing: -1px;
  }
  .brand-tagline {
    font-family: "Open Sans", Arial, sans-serif; font-size: 21px; line-height: 1;
    margin-top: 6px;
  }
  .card-front .brand { right: 35px; top: 30px; text-align: right; }
  .card-front .brand-name { color: var(--brand-blue); }
  .card-front .brand-tagline { color: var(--tagline-blue); }

  .name-marker { position: absolute; left: 0; top: 208px; width: 14px; height: 48px; background: var(--brand-blue); }
  .person-name {
    position: absolute; left: 35px; top: 205px;
    font-size: 26px; font-weight: 600; color: var(--brand-blue); line-height: 1.1;
  }
  .person-role {
    position: absolute; left: 35px; top: 236px;
    font-size: 19px; color: var(--text-dark); line-height: 1;
  }
  .name-rule { position: absolute; left: 177px; right: 35px; top: 253px; height: 2px; background: var(--rule-blue); }

  .contact-list { position: absolute; left: 36px; top: 272px; list-style: none; }
  .contact-list li {
    display: flex; align-items: center; height: 27.5px;
    font-size: 20px; color: var(--text-gray);
  }
  .contact-list svg { width: 18px; height: 18px; margin-right: 10px; fill: var(--brand-blue); flex: none; }

  .social-row { position: absolute; right: 35px; top: 289px; display: flex; gap: 4px; }
  .social-tile { width: 36px; height: 36px; border-radius: 6px; background: var(--accent-blue); }

  .address {
    position: absolute; right: 35px; top: 330px; text-align: right;
    font-style: normal; font-size: 20px; line-height: 26px; color: var(--text-gray);
  }

  .app-badges { position: absolute; right: 30px; top: 38px; display: flex; gap: 14px; }
  .app-badge { width: 44px; height: 48px; background: var(--white); }
  .app-badge-square { border-radius: 8px; }
  .app-badge-circle { border-radius: 50%; width: 46px; }

  .card-back .brand { left: 0; right: 0; top: 160px; text-align: center; }
  .card-back .brand-name { color: var(--white); font-size: 66px; }
  .card-back .brand-tagline { color: var(--white); font-size: 24px; margin-top: 8px; }

  .service-lines {
    position: absolute; left: 0; right: 0; top: 318px; text-align: center;
    font-family: "Roboto Condensed", "Arial Narrow", sans-serif; font-size: 20px; line-height: 31px;
  }
</style>
</head>
<body>
<main class="canvas">

  <section class="card card-front" aria-label="Business card front">
    <div class="brand">
      <div class="brand-name">Velmorix</div>
      <div class="brand-tagline">Every Mile, Every Move</div>
    </div>

    <div class="name-marker"></div>
    <h1 class="person-name">Harold P Simkins</h1>
    <p class="person-role">CEO/Founder</p>
    <div class="name-rule"></div>

    <ul class="contact-list">
      <li>
        <svg viewBox="0 0 24 24" aria-hidden="true"><path d="M6.6 10.8a15.1 15.1 0 0 0 6.6 6.6l2.2-2.2a1 1 0 0 1 1-.25 11.4 11.4 0 0 0 3.6.57 1 1 0 0 1 1 1V20a1 1 0 0 1-1 1A17 17 0 0 1 3 4a1 1 0 0 1 1-1h3.5a1 1 0 0 1 1 1c0 1.25.2 2.45.57 3.57a1 1 0 0 1-.25 1z"/></svg>
        877-410-5526
      </li>
      <li>
        <svg viewBox="0 0 24 24" aria-hidden="true"><path d="M6 2h10l2 2v5H6zM3 10h18a1 1 0 0 1 1 1v8a1 1 0 0 1-1 1H3a1 1 0 0 1-1-1v-8a1 1 0 0 1 1-1zm4 3v2h10v-2z"/></svg>
        573 204 8817
      </li>
      <li>
        <svg viewBox="0 0 24 24" aria-hidden="true"><path d="M2 5h20v14H2zm2 2v.5l8 5 8-5V7l-8 5z"/></svg>
        harold@velmorix.com
      </li>
      <li>
        <svg viewBox="0 0 24 24" aria-hidden="true"><circle cx="12" cy="12" r="10"/><path d="M2 12h20M12 2c3 3 3 17 0 20M12 2c-3 3-3 17 0 20" stroke="#fff" stroke-width="1.4" fill="none"/></svg>
        www.velmorix.com
      </li>
    </ul>

    <div class="social-row" aria-label="Social links">
      <span class="social-tile"></span>
      <span class="social-tile"></span>
      <span class="social-tile"></span>
      <span class="social-tile"></span>
    </div>

    <address class="address">
      2140 Larchwood Drive<br>
      Fairbanks, Alaska 99712
    </address>
  </section>

  <section class="card card-back" aria-label="Business card back">
    <div class="app-badges" aria-label="Mobile apps available">
      <span class="app-badge app-badge-square"></span>
      <span class="app-badge app-badge-circle"></span>
    </div>

    <div class="brand">
      <div class="brand-name">Velmorix</div>
      <div class="brand-tagline">Every Mile, Every Move</div>
    </div>

    <p class="service-lines">
      Fleet tracking efficient and reliable | Family Safety Starts with Velmorix<br>
      Solar GPS Tracker, Lasting &amp; Dependable | Track Anything, Any time, Anyehere
    </p>
  </section>

</main>
</body>
</html>
```